Quorvel Lab - Business Cards & Stationary
Layouts for B-cards, Letterhead, Powerpoint Templates
Quorvel Lab - Business Cards & Stationary -
Creative Brief
Professional
Desmond Pelly
Director of Product Development
4852 Amberfield Lane Dallas, Texas 75391-4418
des.pelly@quorvellabs.example

```html
<!DOCTYPE html>
<html lang="en">
<head>
<meta charset="utf-8">
<title>Quorvel Lab Business Card</title>
<link rel="stylesheet" href="https://fonts.googleapis.com/css2?family=Arimo:wght@400;700&display=swap">
<style>
  :root {
    --backdrop: #e9e6e1;
    --card-light: #ffffff;
    --card-shade: #e4e4e4;
    --ink-dark: #2e2e2e;
    --ink-mid: #555555;
    --brand-gold: #8a6a2c;
    --band-brown: #6b4a1f;
    --band-brown-dark: #4a3112;
    --accent-red: #9c1c22;
    --divider: #9a9a9a;
  }
  * { margin: 0; padding: 0; box-sizing: border-box; }
  html, body {
    width: 1200px; height: 971px; overflow: hidden;
    background: var(--backdrop);
    font-family: "Arimo", Arial, sans-serif;
  }
  .canvas { position: relative; width: 1200px; height: 971px; }
  .card {
    position: absolute;
    width: 566px; height: 329px;
    border-radius: 16px;
    overflow: hidden;
    background: linear-gradient(160deg, var(--card-light) 0%, #f6f6f6 55%, var(--card-shade) 100%);
    box-shadow: 0 6px 18px rgba(0,0,0,0.18);
  }
  .card-front { left: 137px; top: 139px; z-index: 2; }
  .card-back { left: 434px; top: 429px; z-index: 1; }

  .brand {
    position: absolute; left: 74px; top: 64px;
    display: flex; align-items: center; gap: 14px;
  }
  .brand-dot {
    width: 52px; height: 52px; border-radius: 50%;
    background: var(--brand-gold);
  }
  .brand-name {
    font-size: 50px; font-weight: 700; color: var(--brand-gold);
    letter-spacing: -0.5px; line-height: 1;
  }

  .person {
    position: absolute; right: 321px; top: 214px;
    text-align: right;
  }
  .person-name { font-size: 19px; font-weight: 700; color: var(--ink-dark); }
  .person-title { font-size: 11px; color: var(--ink-mid); margin-top: 3px; }

  .divider {
    position: absolute; left: 260px; top: 200px;
    width: 1px; height: 64px; background: var(--divider);
  }
  .contact {
    position: absolute; left: 274px; top: 198px;
    font-size: 13px; line-height: 17px; color: var(--ink-dark);
    list-style: none;
  }
  .contact .label { display: inline-block; width: 40px; }

  .footer-band {
    position: absolute; left: 0; bottom: 0; width: 566px; height: 24px;
  }

  .back-mark {
    position: absolute; right: 26px; bottom: 24px;
    width: 46px; height: 46px; border-radius: 50%;
    background: var(--brand-gold);
  }
</style>
</head>
<body>
<main class="canvas">
  <section class="card card-front" aria-label="Business card front">
    <div class="brand">
      <span class="brand-dot"></span>
      <span class="brand-name">Quorvel Labs</span>
    </div>

    <div class="person">
      <p class="person-name">Desmond Pelly</p>
      <p class="person-title">Director of Product Development</p>
    </div>

    <span class="divider"></span>

    <ul class="contact">
      <li>4852 Amberfield Lane</li>
      <li>Dallas, Texas 75391-4418</li>
      <li><span class="label">Cell:</span>817.555.0142</li>
      <li>Email: des.pelly@quorvellabs.example</li>
    </ul>

    <svg class="footer-band" viewBox="0 0 566 24" preserveAspectRatio="none" aria-hidden="true">
      <defs>
        <linearGradient id="bandBrown" x1="0" y1="0" x2="0" y2="1">
          <stop offset="0" stop-color="var(--band-brown)"/>
          <stop offset="1" stop-color="var(--band-brown-dark)"/>
        </linearGradient>
        <linearGradient id="bandRed" x1="0" y1="0" x2="1" y2="0">
          <stop offset="0" stop-color="#c43a3f"/>
          <stop offset="1" stop-color="var(--accent-red)"/>
        </linearGradient>
      </defs>
      <rect x="0" y="4" width="566" height="20" fill="url(#bandBrown)"/>
      <path d="M330 24 C380 6 430 2 566 0 L566 24 Z" fill="url(#bandRed)"/>
      <path d="M300 24 C350 10 400 6 440 5" stroke="#ffffff" stroke-width="2" fill="none" opacity="0.8"/>
    </svg>
  </section>

  <section class="card card-back" aria-label="Business card back">
    <span class="back-mark"></span>
  </section>
</main>
</body>
</html>
```